Wired Earphone Creative Packaging Design

We would like a creative window box style packaging design for our wired earphone

Size: 6” x 3.5” x 1.5” (enclosed die-cut drawing)
Material: E Flute Paper box
Type: Window Box style
Design features we prefer: friendly, playful, creative, trendy, unique, High tech.
Competitors: Enclosed
Requirement:AI file is preferred

Enclosed are product pictures, marketing materials and competitor designs for your reference.

Any further questions, please feel free to ask.
Updates

So designers get more time to design

Target Market(s)

13-40 Year Olds

Industry/Entity Type

Audio

Colors

Designer to choose colors to be used in the design.

Requirements
Must have
• Window, selling point, creative

```html
<!DOCTYPE html>
<html lang="en">
<head>
<meta charset="utf-8">
<title>VB-2 Customizable Earbuds – Front and Side Panels</title>
<link href="https://fonts.googleapis.com/css2?family=Bebas+Neue&family=Oswald:wght@400;600;700&display=swap" rel="stylesheet">
<style>
  :root {
    --bg: #3a3950;
    --blue: #1fa6e0;
    --blue-light: #5cc6f0;
    --blue-deep: #0f86c4;
    --window: #cdeefb;
    --white: #ffffff;
    --side: #eeeff1;
    --side-shade: #d9dbdf;
    --ink: #2d2d33;
  }
  * { box-sizing: border-box; margin: 0; padding: 0; }
  html, body { width: 882px; height: 1200px; overflow: hidden; background: var(--bg); }
  .canvas { position: relative; width: 882px; height: 1200px; }

  /* Front panel */
  .front {
    position: absolute; left: 41px; top: 120px; width: 560px; height: 960px;
    background: linear-gradient(160deg, var(--blue-light) 0%, var(--blue) 45%, var(--blue-deep) 100%);
    overflow: hidden;
  }
  .front-sheen {
    position: absolute; inset: 0;
    background: linear-gradient(180deg, rgba(255,255,255,0.18), rgba(255,255,255,0) 30%, rgba(255,255,255,0) 80%, rgba(255,255,255,0.12));
  }
  .model { position: absolute; left: 26px; top: 52px; color: var(--white); }
  .model-name { font-family: 'Bebas Neue', sans-serif; font-size: 80px; line-height: 0.9; letter-spacing: 2px; }
  .model-note { font-family: 'Oswald', sans-serif; font-weight: 600; font-size: 13px; line-height: 1.15; text-transform: uppercase; margin-top: 4px; }
  .title-card {
    position: absolute; right: 0; top: 62px; width: 320px; height: 128px;
    background: var(--white); padding: 12px 16px;
    font-family: 'Oswald', sans-serif; color: var(--ink); text-transform: uppercase;
  }
  .title-line { font-weight: 600; font-size: 36px; line-height: 1; letter-spacing: 0.5px; }
  .title-tag {
    display: inline-block; margin: 5px 0 4px; padding: 0 8px;
    background: var(--blue); color: var(--white); font-weight: 700; font-size: 17px; line-height: 1.25;
    border: 2px solid var(--blue-deep);
  }
  .window {
    position: absolute; left: 38px; top: 225px; width: 522px; height: 560px;
    background: linear-gradient(135deg, rgba(255,255,255,0.75), var(--window) 40%, rgba(180,228,248,0.9));
    border-radius: 4px 0 0 4px;
  }
  .features {
    position: absolute; left: 0; bottom: 0; width: 100%; height: 175px;
    display: flex; justify-content: space-around; align-items: flex-start; padding: 28px 14px 0;
  }
  .feature { width: 100px; text-align: center; color: var(--white); font-family: 'Oswald', sans-serif; }
  .feature-icon { display: block; margin: 0 auto 8px; }
  .feature-label { font-size: 12px; font-weight: 600; text-transform: uppercase; line-height: 1.15; }

  /* Side panel */
  .side {
    position: absolute; left: 601px; top: 120px; width: 240px; height: 960px;
    background: linear-gradient(90deg, var(--side) 0%, var(--white) 55%, var(--side-shade) 100%);
    overflow: hidden;
  }
  .side-title {
    position: absolute; left: 212px; bottom: 60px; width: 640px; height: 184px;
    transform-origin: left bottom; transform: rotate(-90deg);
    display: flex; flex-direction: column; justify-content: center;
    font-family: 'Oswald', sans-serif; color: var(--ink); text-transform: uppercase;
  }
  .side-line { font-weight: 600; font-size: 66px; line-height: 1; letter-spacing: 1px; }
  .side-tag {
    align-self: flex-start; margin: 6px 0;
    padding: 0 10px; background: var(--blue); color: var(--white);
    border: 2px solid var(--blue-deep); font-weight: 700; font-size: 26px; line-height: 1.25;
  }
</style>
</head>
<body>
<div class="canvas">
  <section class="front">
    <div class="front-sheen"></div>

    <div class="model">
      <div class="model-name">VB-2</div>
      <div class="model-note">Includes<br>multi-function<br>controller</div>
    </div>
    <div class="title-card">
      <div class="title-line">Customizable</div>
      <div class="title-tag">Stereo In-Ear</div>
      <div class="title-line">Earbuds</div>
    </div>

    <div class="window" role="img" aria-label="Clear die-cut window showing the earbuds inside"></div>

    <footer class="features">
      <div class="feature">
        <svg class="feature-icon" width="54" height="54" viewBox="0 0 64 64"><circle cx="32" cy="32" r="29" fill="none" stroke="#fff" stroke-width="3"/><text x="32" y="38" text-anchor="middle" font-family="Oswald, sans-serif" font-size="17" font-weight="700" fill="#fff">3.5</text></svg>
        <div class="feature-label">Customizable color tape</div>
      </div>
      <div class="feature">
        <svg class="feature-icon" width="54" height="54" viewBox="0 0 64 64"><circle cx="32" cy="32" r="29" fill="none" stroke="#fff" stroke-width="3"/><rect x="26" y="16" width="12" height="22" rx="6" fill="#fff"/><path d="M20 32a12 12 0 0 0 24 0M32 44v6" fill="none" stroke="#fff" stroke-width="3"/></svg>
        <div class="feature-label">In-line mic</div>
      </div>
      <div class="feature">
        <svg class="feature-icon" width="54" height="54" viewBox="0 0 64 64"><circle cx="32" cy="32" r="29" fill="none" stroke="#fff" stroke-width="3"/><rect x="25" y="14" width="14" height="36" rx="7" fill="none" stroke="#fff" stroke-width="3"/><circle cx="32" cy="32" r="3" fill="#fff"/></svg>
        <div class="feature-label">Universal control</div>
      </div>
      <div class="feature">
        <svg class="feature-icon" width="54" height="54" viewBox="0 0 64 64"><circle cx="32" cy="32" r="29" fill="none" stroke="#fff" stroke-width="3"/><circle cx="22" cy="36" r="5" fill="#fff"/><circle cx="32" cy="34" r="7" fill="#fff"/><circle cx="44" cy="32" r="9" fill="#fff"/></svg>
        <div class="feature-label">3 tip sizes</div>
      </div>
      <div class="feature">
        <svg class="feature-icon" width="54" height="54" viewBox="0 0 64 64"><circle cx="32" cy="32" r="29" fill="none" stroke="#fff" stroke-width="3"/><path d="M18 40c0-12 8-20 18-20 6 0 10 4 10 9s-4 8-9 8h-5v6H18z" fill="#fff"/></svg>
        <div class="feature-label">Ergonomic design</div>
      </div>
    </footer>
  </section>

  <section class="side">
    <div class="side-title">
      <div class="side-line">Customizable</div>
      <div class="side-tag">Stereo In-Ear</div>
      <div class="side-line">Earbuds</div>
    </div>
  </section>
</div>
</body>
</html>
```